Business Card Design

I run an executive search and head hunting company.
My areas of business is within financial services and I cover, primarily sales and trading.

I am looking for a double sided, black business card and would like to keep the design fairly simple. Name to front and details on the reverse.

I would require a logo - some logo ideas.

*****Just some idea I am playing with - a white out halo over the "i" in Dorian.
A quill or feather somewhere within the layout. Above the Dorian Wells & Coyle ? beneath it ? etc......

I have attached something I quite like but the whole creativity and layout is down to you. I am thinking to have the "&" in between Dorian Wells & Coyle, maybe white out perhaps and may have it spot gloss uv'd when it comes to print.

I am pretty open minded though !

Target Market(s)

financial services - brokers and investment banking

Industry/Entity Type

Financial

Contact Information for Business Card

Dorian Wells & Coyle
No 9 The Yard
63 Tilbury Lane
Brentwood
Essex
CM17 8RW

Telephone - + 44 (0)1277 639 518
Mobile -+ 44 (0) 7700 954 173
email - oliver@dorianwellscoyle.co.uk
web - www.dorianwellscoyle.co.uk

Oliver Coyle
Managing Director

Colors

Designer to choose colors to be used in the design.

Requirements
Should not have
• Finance - brokers investment banking.

```html
<!DOCTYPE html>
<html lang="en">
<head>
<meta charset="utf-8">
<title>Dorian Wells &amp; Coyle — Business Card</title>
<link href="https://fonts.googleapis.com/css2?family=Playfair+Display:wght@700;800&display=swap" rel="stylesheet">
<style>
  :root {
    --backdrop: #d9d9d7;
    --card-black: #121212;
    --card-edge: #1c1c1c;
    --emboss-grey: #5d5d5d;
    --emboss-light: #7a7a7a;
    --detail-grey: #6a6a6a;
  }
  * { margin: 0; padding: 0; box-sizing: border-box; }
  html, body {
    width: 1200px;
    height: 1200px;
    overflow: hidden;
    background: var(--backdrop);
  }
  .sheet {
    width: 1200px;
    height: 1200px;
    display: flex;
    flex-direction: column;
    align-items: center;
    justify-content: center;
    gap: 64px;
  }
  .card {
    position: relative;
    width: 760px;
    height: 434px;
    background: linear-gradient(160deg, var(--card-edge) 0%, var(--card-black) 55%, #0c0c0c 100%);
    font-family: "Playfair Display", Georgia, serif;
    font-weight: 700;
    color: var(--emboss-grey);
  }
  .company-mark {
    position: absolute;
    top: 42px;
    left: 48px;
    font-size: 22px;
    color: var(--emboss-light);
    letter-spacing: 0.5px;
  }
  .card-front .company-name {
    position: absolute;
    right: 56px;
    top: 120px;
    text-align: right;
    font-size: 76px;
    line-height: 1.02;
    font-weight: 800;
    color: var(--emboss-grey);
  }
  .card-back .person {
    position: absolute;
    left: 92px;
    top: 150px;
    font-size: 27px;
    color: var(--emboss-grey);
  }
  .card-back .contact-details {
    position: absolute;
    left: 60px;
    top: 232px;
    list-style: none;
    font-size: 19px;
    line-height: 1.3;
    color: var(--detail-grey);
  }
</style>
</head>
<body>
  <main class="sheet">
    <section class="card card-front" aria-label="Card front">
      <div class="company-mark">Dorian Wells &amp; Coyle</div>
      <h1 class="company-name">Dorian Wells<br>&amp; Coyle</h1>
    </section>

    <section class="card card-back" aria-label="Card back">
      <div class="company-mark">Dorian Wells &amp; Coyle</div>
      <p class="person">Oliver Coyle Managing Director</p>
      <ul class="contact-details">
        <li>No 9 The Yard 63 Tilbury Lane Brentwood Essex CM17 8RW</li>
        <li>Telephone - + 44 (0)1277 639 518 Mobile - 07700 954 173</li>
        <li>email - oliver@dorianwellscoyle.co.uk</li>
        <li>web - www.dorianwellscoyle.co.uk</li>
      </ul>
    </section>
  </main>
</body>
</html>
```